Cheese Company Needs Product Label Design

Hello Designers. We are a cheese manufacturer and are looking for a label design for our new product "Fresh Mozzarella". The cheese balls come in a container that includes Sun-Dried Tomato with Parsley and Garlic marinated in oil.Here are the requirements:

1. LABEL: There will be a main circular label and a side label. The main circular label should be 3.83" in diameter. The side rectangular label should be 1.5" Length 3.25" Width.

2. DESIGN (LOGO): The company logo (attached) should be placed on the top in middle just like in the "product example" file that is included in the project.

3. DESIGN (PRODUCT NAME): The product name "FRESH MOZZARELLA" should be below the logo and be big in capital letters straight. Also include "ALL NATURAL" right above the name just like the "product example". Include "ORGANIC" icon somewhere on it.

4. DESIGN (PRODUCT DESCRIPTION): The product description "SUN-DRIED TOMATO and PARSLEY" should be below the product name. Make it look fancy.

5. DESIGN (PRODUCT PICTURE): I would like you to create a product drawing of many mozzarella balls with Sun-Dried Tomato and Parsley in it below the product description. Make sure it is attractive and pops-out on the label. Look at the "product example" to get an idea but please make sure you don't make it exactly the same. This is important as it needs to be arranged in such a way to not be too similar. Look at the file "inspiration 4" to see how it looks like.

6. DESIGN (BACKGROUND): The background of the picture should reflect a natural, organic, elegant scene. Think mountains, valleys, rivers flowing, nature, cows in the field and sun shining. I attached an "inspiration" photos here so you can get an idea. Make sure that the product is the main focus and not the background. It should be sophisticated with not too much color. Include a small border around the whole label.
DO NOT MAKE IT LOOK CARTOONISH!

7. WEIGHT: The weight of the product should be in the lower right corner and should say "NET WT. 12oz" and below that "(340g)".

8. KOSHER: The tablet kosher symbol should be on the lower right corner. Please look it up how it looks like.

9. SIDE LABEL: The side label should maintain the same color scheme as the main label similar to the "product example" attached here. It should have the Nutritional Facts attached, the Bar Code, and the "DISTRIBUTED BY: BRAVOLT LLC. 482 ELMCREST AVENUE, GLEN HARBOR, NY 11592". You can arrange it how you see fit but the Bar Code should be at least 1/3 of the label. Refer to the "product example" and keep close to its design. Put "MADE IN USA" on the right hand side. The last few things you need to do is put the Ingredients List below the Nutritional Facts as shown in the "product example", put the website "WWW.BRAVOLTFOODS.COM" below the Ingredients List, and put three social media icons going Facebook, Twitter, Instagram referring to @BravoltFoods somewhere near the bottom in it. Put the plant number on the side "PLANT NO. 52-7049" on it. Type out on the same side in bold letters to "KEEP REFRIGERATED".

10. FINAL: Thank you for accepting this project. As a main objective the label needs to look sophisticated and a high quality product. You can add your own twist on the design and keep it close to the rules. The Bar Code is not included in the files and will be given once we choose you as a designer for this. We also attached our "previous products" so you can get an idea of the type of company we are.

Target Market(s)

Cheese lovers, people who like snacks, natural food eaters.

Industry/Entity Type

Dairy Farm

Font styles to use
Serif
Script

Colors
ffffff
cadf82
f04a50
85cae6

Requirements
Must have
• All the point in the product description
Nice to have
• The points at a minimum.
Should not have
• Everything is explained. Do not make it look cartoonish!

```html
<!DOCTYPE html>
<html lang="en">
<head>
<meta charset="utf-8">
<title>Bravolt Fresh Mozzarella – Label Set</title>
<link href="https://fonts.googleapis.com/css2?family=Playfair+Display:wght@400;700;900&family=Open+Sans:wght@400;600;700;800&display=swap" rel="stylesheet">
<style>
  :root{
    --bg:#e6e6e4;
    --rim:#e58d2a;
    --rim-dark:#c9731c;
    --sky-light:#fff6c9;
    --sky:#fbd75a;
    --field:#f2b534;
    --brand-red:#b5232a;
    --band-green:#3f8f2e;
    --ink:#5a2c0c;
    --white:#ffffff;
    --tomato:#d8382f;
  }
  *{box-sizing:border-box;margin:0;padding:0}
  html,body{width:1200px;height:889px;overflow:hidden;background:var(--bg)}
  body{position:relative;font-family:"Open Sans",sans-serif}

  /* ---------- main circular label ---------- */
  .main-label{
    position:absolute;left:40px;top:165px;width:560px;height:560px;border-radius:50%;
    background:var(--rim);padding:22px;
  }
  .main-label__face{
    position:relative;width:100%;height:100%;border-radius:50%;overflow:hidden;
    background:radial-gradient(circle at 50% 38%,var(--sky-light) 0%,var(--sky) 45%,var(--field) 100%);
  }
  .landscape{position:absolute;left:0;right:0;bottom:0;height:60%;
    background:linear-gradient(180deg,rgba(242,181,52,0) 0%,rgba(236,166,40,.55) 60%,rgba(226,150,32,.8) 100%)}
  .brand{position:absolute;top:40px;left:0;right:0;display:flex;justify-content:center;align-items:center;gap:8px}
  .brand__dot{width:14px;height:14px;border-radius:50%;background:var(--brand-red)}
  .brand__name{font-family:"Open Sans",sans-serif;font-weight:800;font-size:30px;color:var(--brand-red);letter-spacing:.5px}
  .all-natural{position:absolute;top:92px;right:118px;font-family:"Playfair Display",serif;font-size:24px;color:#3b2410}
  .product-name{position:absolute;top:118px;left:0;right:0;text-align:center;
    font-family:"Playfair Display",serif;font-weight:900;font-size:54px;color:var(--brand-red);
    letter-spacing:-1px;transform:scaleX(.78);white-space:nowrap}
  .flavor-band{position:absolute;top:200px;left:50%;transform:translateX(-50%) rotate(-3deg);
    background:var(--band-green);color:var(--white);font-size:19px;font-weight:600;padding:6px 22px;white-space:nowrap}
  .product-art{position:absolute;left:50%;top:258px;transform:translateX(-50%);width:230px;height:190px;border-radius:50%;
    background:radial-gradient(ellipse at 50% 45%,#ffffff 0%,#f4f4f2 60%,#dcdcd8 100%)}
  .tomato-art{position:absolute;left:70px;top:330px;width:70px;height:90px;border-radius:40%;
    background:radial-gradient(circle at 40% 40%,#f06a52,var(--tomato) 60%,#9e1f1a)}
  .kosher{position:absolute;right:82px;top:344px;width:20px;height:20px;border:2px solid #2a1a0c;border-radius:3px}
  .net-wt{position:absolute;right:54px;top:372px;font-family:"Playfair Display",serif;font-size:13px;color:#2a1a0c;text-align:center;line-height:1.2}

  /* ---------- side label ---------- */
  .side-label{position:absolute;left:640px;top:310px;width:520px;height:260px;background:var(--rim);display:flex;padding:14px 12px 12px 26px;color:var(--ink)}
  .distributor{position:absolute;left:4px;top:10px;height:240px;writing-mode:vertical-rl;transform:rotate(180deg);
    font-size:7px;letter-spacing:.2px;color:var(--ink);text-align:center}
  .side-label__info{flex:1;display:flex;flex-direction:column;padding-right:12px}
  .side-label__title{font-size:14px;font-weight:600;margin-bottom:6px}
  .nutrition{border-collapse:collapse;width:100%;font-size:8px}
  .nutrition td,.nutrition th{border:1px solid var(--ink);padding:2px 4px;text-align:center;font-weight:400}
  .nutrition th:first-child{font-size:11px;font-weight:700;text-align:left;line-height:1}
  .nutrition td:first-child{text-align:left}
  .ingredients{font-size:8px;margin-top:6px;line-height:1.3}
  .ingredients b{font-weight:800}
  .web-row{margin-top:auto;display:flex;gap:12px;align-items:center;font-size:10px;font-weight:700;color:var(--white)}
  .side-label__panel{width:150px;background:var(--white);display:flex;flex-direction:column;align-items:center;padding:16px 10px 10px}
  .panel-brand{display:flex;align-items:center;gap:5px;font-weight:800;font-size:18px;color:var(--brand-red)}
  .panel-brand span.dot{width:9px;height:9px;border-radius:50%;background:var(--brand-red)}
  .keep-cold{margin-top:10px;font-size:10px;font-weight:800;color:var(--ink)}
  .plant{font-size:8px;color:var(--ink);margin-top:2px}
  .made-in{margin-top:auto;align-self:flex-end;font-size:10px;color:var(--ink)}
</style>
</head>
<body>

<section class="main-label" aria-label="Main circular label">
  <div class="main-label__face">
    <div class="landscape" role="img" aria-label="Soft golden countryside with hills, trees and grazing cows"></div>
    <div class="brand"><span class="brand__dot"></span><span class="brand__name">BRAVOLT</span></div>
    <div class="all-natural">All natural</div>
    <h1 class="product-name">FRESH MOZZARELLA</h1>
    <div class="flavor-band">Sundried Tomato &amp; Parsley</div>
    <div class="tomato-art" role="img" aria-label="Ripe red tomatoes"></div>
    <div class="product-art" role="img" aria-label="White bowl of mozzarella balls with sun-dried tomato and parsley"></div>
    <div class="kosher" aria-label="Kosher certification mark"></div>
    <div class="net-wt">NET WT. 12oz<br>(340g)</div>
  </div>
</section>

<section class="side-label" aria-label="Side label">
  <div class="distributor">DISTRIBUTED BY: BRAVOLT LLC. 482 ELMCREST AVENUE, GLEN HARBOR, NY 11592</div>
  <div class="side-label__info">
    <div class="side-label__title">Formaggio 12 oz Sundried Tomato &amp; Parsley</div>
    <table class="nutrition">
      <tr><th>Nutrition<br>Facts</th><td>dummy</td><td>dummy</td><td>dummy</td><td>dummy</td></tr>
      <tr><td>Dummy text</td><td>printing</td><td>1234,7</td><td>printing</td><td>1234,7</td></tr>
      <tr><td>Dummy text</td><td>printing</td><td>1234,7</td><td>printing</td><td>1234,7</td></tr>
      <tr><td>Dummy text</td><td>printing</td><td>1234,7</td><td>printing</td><td>1234,7</td></tr>
      <tr><td>Dummy text</td><td>printing</td><td>1234,7</td><td>printing</td><td>1234,7</td></tr>
      <tr><td>Dummy text of the printing and</td><td>printing</td><td>1234,7</td><td>printing</td><td>1234,7</td></tr>
    </table>
    <p class="ingredients"><b>INGREDIENTS:</b> Lorem Ipsum is simply dummy text of the printing and typesetting industry. Lorem Ipsum has been the industry's standard dummy.</p>
    <div class="web-row"><span>WWW.BRAVOLTFOODS.COM</span><span>@BravoltFoods</span></div>
  </div>
  <div class="side-label__panel">
    <div class="panel-brand"><span class="dot"></span>BRAVOLT</div>
    <div class="keep-cold">KEEP REFRIGERATED</div>
    <div class="plant">PLANT NO. 52-7049</div>
    <div class="made-in">Made in USA</div>
  </div>
</section>

</body>
</html>
```